Bridal Beauty Expert 5 page Website

Modern 5 page website including: home page, Bridal Experts, services, gallery, and book me. Home page to include photo slideshow and contact information for stylist. The Bridal a Experts section will include short biography and photos of each bridal expert 3-4. Services page will include list and description of services and pricing. Gallery will contain work divided in the hair and makeup category. The book me page will contain an active booking tab with drop down service and customer information.

Target Market(s)

Brides, ages 21 to 45

Industry/Entity Type

Hair And Beauty

Coding

Coded - Design and coding required

Number of Pages Required

5+ page

Font styles to use
Serif
Decorative
Script

Colors
faa54b
97b8d9

Requirements
Must have
• Photo slideshow, photo gallery
Nice to have
• Scrolling slide show on home page

```html
<!DOCTYPE html>
<html lang="en">
<head>
<meta charset="utf-8">
<title>Veil &amp; Velvet — Book Me</title>
<link rel="stylesheet" href="https://fonts.googleapis.com/css2?family=Roboto:wght@400;500&family=Raleway:wght@400;500;600&display=swap">
<style>
  :root {
    --orange: #f9a54b;
    --teal: #8fcdc7;
    --teal-deep: #7fc4bd;
    --white: #ffffff;
    --ink-light: #f4fbfa;
    --form-line: #ffffff;
    --label: #f9a54b;
  }
  * { box-sizing: border-box; margin: 0; padding: 0; }
  html, body { width: 873px; height: 1200px; overflow: hidden; background: var(--white); }
  body { font-family: "Roboto", Arial, sans-serif; position: relative; }
  .canvas { position: relative; width: 873px; height: 1200px; overflow: hidden; }

  /* header */
  .nav-pill {
    position: absolute; top: 47px; height: 29px; border-radius: 15px;
    background: var(--orange); color: var(--white);
    font: 500 12px/29px "Roboto", Arial, sans-serif; text-align: center; text-decoration: none;
  }
  .nav-pill.is-active { background: var(--teal); }
  .brand {
    position: absolute; left: 364px; top: 44px; width: 141px; height: 34px;
    display: flex; align-items: center; justify-content: center; gap: 6px;
    color: var(--teal-deep); font: 500 17px/1 "Raleway", Arial, sans-serif; white-space: nowrap;
  }
  .brand-dot { width: 8px; height: 8px; border-radius: 50%; background: var(--teal-deep); }

  .photo { position: absolute; display: block; }

  /* booking */
  .tabs { position: absolute; top: 376px; left: 0; width: 873px; }
  .tab {
    position: absolute; height: 22px; border-radius: 11px; background: var(--white);
    color: #333; font: 400 11px/22px "Roboto", Arial, sans-serif; text-align: center;
  }
  .tab.is-active { background: var(--orange); color: var(--white); }
  .divider-ornament { position: absolute; left: 408px; top: 424px; width: 58px; height: 6px; border-radius: 3px; background: rgba(255,255,255,0.75); }

  .field-label { position: absolute; left: 210px; color: var(--label); font: 400 12px/1 "Roboto", Arial, sans-serif; }
  .field {
    position: absolute; left: 204px; width: 461px; height: 37px;
    border: 1.5px solid var(--form-line); border-radius: 10px;
    color: var(--white); font: 400 13px/34px "Roboto", Arial, sans-serif; padding-left: 17px;
  }
  .field-addon { position: absolute; right: 0; top: 0; width: 43px; height: 100%; border-left: 1.5px solid var(--form-line); display: flex; align-items: center; justify-content: center; }
  .submit {
    position: absolute; left: 286px; top: 726px; width: 291px; height: 38px;
    border: 1.5px solid var(--white); border-radius: 10px; background: var(--orange);
    color: var(--white); font: 500 17px/35px "Roboto", Arial, sans-serif; text-align: center;
  }

  /* footer */
  .footer-heading { position: absolute; color: var(--white); font: 500 16px/1 "Raleway", Arial, sans-serif; }
  .about-text { position: absolute; left: 95px; top: 971px; width: 228px; color: var(--white); font: 400 8.6px/1.55 "Roboto", Arial, sans-serif; }
  .social { position: absolute; left: 93px; top: 1083px; display: flex; gap: 3px; }
  .social-dot { width: 27px; height: 27px; border-radius: 50%; background: var(--white); }
  .copyright { position: absolute; left: 92px; top: 1139px; color: var(--white); font: 400 8.6px/1 "Roboto", Arial, sans-serif; }

  .post-list { position: absolute; left: 366px; top: 977px; width: 160px; list-style: none; }
  .post { position: relative; padding-left: 13px; margin-bottom: 11px; color: var(--white); font: 400 8.8px/1.5 "Roboto", Arial, sans-serif; }
  .post::before { content: "›"; position: absolute; left: 0; top: -2px; font-size: 12px; }
  .post-date { display: block; }

  .search { position: absolute; left: 570px; top: 977px; width: 214px; height: 20px; border-bottom: 1px solid var(--white); color: var(--white); font: 400 9px/16px "Roboto", Arial, sans-serif; }
  .search svg { position: absolute; right: 3px; top: 3px; }
  .contact { position: absolute; left: 570px; display: flex; gap: 11px; color: var(--white); font: 400 11px/1.45 "Roboto", Arial, sans-serif; }
  .contact-icon { width: 18px; flex: none; display: flex; justify-content: center; }
</style>
</head>
<body>
<div class="canvas">

  <header>
    <a class="nav-pill" style="left:63px;width:62px">Home</a>
    <a class="nav-pill" style="left:151px;width:79px">About me</a>
    <a class="nav-pill" style="left:258px;width:76px">Services</a>
    <div class="brand"><span class="brand-dot"></span>Veil &amp; Velvet</div>
    <a class="nav-pill" style="left:542px;width:71px">Gallery</a>
    <a class="nav-pill is-active" style="left:647px;width:77px">Book me</a>
    <a class="nav-pill" style="left:746px;width:64px">Login</a>
  </header>

  <svg class="photo" style="left:63px;top:117px" width="747" height="180" viewBox="0 0 747 180" role="img" aria-label="Banner photo of a bride with a tiara in a warm sunlit garden">
    <defs>
      <linearGradient id="heroTone" x1="0" y1="0" x2="1" y2="0">
        <stop offset="0" stop-color="#5a4a36"/>
        <stop offset="0.3" stop-color="#b79672"/>
        <stop offset="0.45" stop-color="#e7d3bd"/>
        <stop offset="0.62" stop-color="#8a6a45"/>
        <stop offset="0.85" stop-color="#6e6a2c"/>
        <stop offset="1" stop-color="#3d3a22"/>
      </linearGradient>
    </defs>
    <rect width="747" height="180" fill="url(#heroTone)"/>
    <path d="M0 180 L0 179 Q373.5 107 747 179 L747 180 Z" fill="#ffffff"/>
  </svg>

  <svg class="photo" style="left:63px;top:307px" width="747" height="610" viewBox="0 0 747 610" role="img" aria-label="Background photo of a bride in a white gown seated on a gilded sofa">
    <defs>
      <linearGradient id="bookingTone" x1="0" y1="0" x2="1" y2="1">
        <stop offset="0" stop-color="#6b625c"/>
        <stop offset="0.4" stop-color="#8a8079"/>
        <stop offset="0.7" stop-color="#7a6f66"/>
        <stop offset="1" stop-color="#5d554f"/>
      </linearGradient>
    </defs>
    <path d="M0 37 Q373.5 -37 747 37 L747 543 Q373.5 575 0 543 Z" fill="url(#bookingTone)"/>
  </svg>

  <section class="booking">
    <div class="tabs">
      <span class="tab is-active" style="left:295px;width:79px">Book 24/7</span>
      <span class="tab" style="left:388px;width:101px">Gift Certificates</span>
      <span class="tab" style="left:505px;width:65px">Reviews</span>
    </div>
    <span class="divider-ornament" role="img" aria-label="Small flourish divider"></span>

    <span class="field-label" style="top:466px">Service(required)</span>
    <div class="field" style="top:485px">Select Service
      <span class="field-addon"><svg width="12" height="7" viewBox="0 0 12 7"><path d="M0 0 H12 L6 7 Z" fill="#fff"/></svg></span>
    </div>

    <span class="field-label" style="top:546px">Service Provider (optional)</span>
    <div class="field" style="top:565px">Select Any Service Provider
      <span class="field-addon"><svg width="12" height="7" viewBox="0 0 12 7"><path d="M0 0 H12 L6 7 Z" fill="#fff"/></svg></span>
    </div>

    <span class="field-label" style="top:626px">Date</span>
    <div class="field" style="top:646px">First Available
      <span class="field-addon"><svg width="15" height="15" viewBox="0 0 15 15" fill="none" stroke="#fff" stroke-width="1.3"><rect x="1" y="2.5" width="13" height="11.5" rx="1.5"/><path d="M1 6 H14 M4.5 0.5 V4 M10.5 0.5 V4"/><path d="M4 8.5h1.5M7 8.5h1.5M10 8.5h1.5M4 11h1.5M7 11h1.5" stroke-width="1.2"/></svg></span>
    </div>

    <div class="submit">Submit</div>
  </section>

  <svg class="photo" style="left:63px;top:862px" width="747" height="312" viewBox="0 0 747 312" aria-hidden="true">
    <path d="M0 0 Q373.5 104 747 0 L747 312 L0 312 Z" fill="var(--teal)"/>
  </svg>

  <footer>
    <h3 class="footer-heading" style="left:95px;top:942px">About us</h3>
    <p class="about-text">We love weddings and all that entails, especially seeing people happily planning the biggest day of their life. We are proud to bring the best people together to make planning that “big day” easier by providing important and reliable resources, answers and solutions.</p>
    <h3 class="footer-heading" style="left:94px;top:1060px">Get Social</h3>
    <div class="social">
      <span class="social-dot"></span><span class="social-dot"></span><span class="social-dot"></span><span class="social-dot"></span><span class="social-dot"></span><span class="social-dot"></span><span class="social-dot"></span>
    </div>
    <p class="copyright">Copyright 2015 © Veil &amp; Velvet .All rights reserved.</p>

    <h3 class="footer-heading" style="left:375px;top:942px">Recent Posts</h3>
    <ul class="post-list">
      <li class="post">This is a Sticky post<span class="post-date">September 16, 2014</span></li>
      <li class="post">This Post Looks Beautiful even Title<span class="post-date">September 12, 2014</span></li>
      <li class="post">This is a video Post<span class="post-date">September 11, 2014</span></li>
      <li class="post">Satisfaction Lies in the Effort<span class="post-date">August 21, 2014</span></li>
    </ul>

    <h3 class="footer-heading" style="left:570px;top:942px">Search Something</h3>
    <div class="search">Search...
      <svg width="11" height="11" viewBox="0 0 11 11" fill="none" stroke="#fff" stroke-width="1.3"><circle cx="4.5" cy="4.5" r="3.6"/><path d="M7.2 7.2 L10.3 10.3"/></svg>
    </div>

    <div class="contact" style="top:1019px">
      <span class="contact-icon"><svg width="17" height="15" viewBox="0 0 17 15"><path d="M8.5 0 L17 7.5 H14.5 V15 H10.5 V10 H6.5 V15 H2.5 V7.5 H0 Z" fill="#fff"/></svg></span>
      <span>2280 Larkspur Avenue<br>Suite 310 Fairhaven, MN 55990</span>
    </div>
    <div class="contact" style="top:1057px">
      <span class="contact-icon"><svg width="17" height="12" viewBox="0 0 17 12" fill="none" stroke="#fff" stroke-width="1.4"><rect x="0.7" y="0.7" width="15.6" height="10.6"/><path d="M0.7 0.7 L8.5 7 L16.3 0.7"/></svg></span>
      <span>hello@veilvelvet.example</span>
    </div>
    <div class="contact" style="top:1084px">
      <span class="contact-icon"><svg width="15" height="15" viewBox="0 0 15 15"><path d="M3 0.5 L5.5 3.8 L4 5.6 C5 7.8 7.2 10 9.4 11 L11.2 9.5 L14.5 12 L12.8 14.5 C6.5 14 1 8.5 0.5 2.2 Z" fill="#fff"/></svg></span>
      <span>555.014.1900</span>
    </div>
    <div class="contact" style="top:1111px">
      <span class="contact-icon"><svg width="17" height="15" viewBox="0 0 17 15"><path d="M1 4 C1 1 16 1 16 4 L16 5.5 L12.5 5.5 L12 3.8 C10 3.2 7 3.2 5 3.8 L4.5 5.5 L1 5.5 Z" fill="#fff"/><path d="M3 15 L4.5 7.5 H12.5 L14 15 Z" fill="#fff"/></svg></span>
      <span>555.014.1922</span>
    </div>
  </footer>

</div>
</body>
</html>
```